Vintage look or abstract painting for singer songwriter

The artist and album are titled "Captain Wren's Parade". The music is very organic and real. Influences include Dale morrow, Carl Hennaway, quiet lanterns. There's a touch of Americana and the artist is British. He had a few ideas relating to railroad cafe's, old farmhouse paintings or old Punch and Judy photographs. The album is a collection of great stories. A former ballerina also features heavily. He likes water colours and abstract art.

So we've had quite a few designs through with a cowboy/western theme. I think we have enough of those theme's. So avoid the cowboy, horses and boots look from now on. Although the look and feel of what's come through is very good. Would be good to have something more landscape based. The album starts with a song called Open Fields, which is very optimistic and full of energy and the album closes with a song called When the last bells toll which is very dark and descends in to chaos, noise and a big explosion leaving a feeling of desperation, uncertainty and the dust settling. So the album progresses from the one extreme to the other. So it's almost like Purgatory in-between. Not sure if any of that helps and I understand the artist has been pretty vague here and it's a tough outline to pick something out. But that's the way the music has been for the musicians on the record and he just loves seeing what people come up with.

Target Market(s)

Authentic music lovers of all ages. Probably people who still like to buy cd's and to whom the cover is important. Nothing modern or sparkly!

Industry/Entity Type

Painting

Font styles to use
Decorative
Script

Requirements
Must have
• The artist doesn't need to feature on the cover. His look is kind of a character. boots, cool hat, long hair, tattoos, trench coat. America folky feel could be good. Nothing rock!!
Nice to have
• Maybe a painting or illustration.
Should not have
• Anything too rock. His main instrument is an halvorna acoustic, so no Brockett stacks on this record!

```html
<!DOCTYPE html>
<html lang="en">
<head>
<meta charset="utf-8">
<title>Captain Wren's Parade</title>
<link rel="stylesheet" href="https://fonts.googleapis.com/css2?family=Cormorant+Garamond:wght@500&display=swap">
<style>
  :root {
    --paper: #f3efbf;
    --paper-edge: #e8e09f;
    --dusk-deep: #22174f;
    --dusk-ink: #352a6e;
    --dusk-mid: #5b4388;
    --dusk-mauve: #8a6a98;
    --dusk-rose: #cf9495;
    --dusk-glow: #ecc3a4;
    --rock-shadow: #3a2356;
    --title-ink: #f3ecc4;
  }
  html, body {
    margin: 0;
    padding: 0;
    width: 1200px;
    height: 1200px;
    overflow: hidden;
    background: var(--paper);
  }
  .cover {
    position: relative;
    width: 1200px;
    height: 1200px;
    background: radial-gradient(circle at 50% 50%, var(--paper) 62%, var(--paper-edge) 100%);
  }
  .cover__painting {
    position: absolute;
    inset: 0;
    width: 1200px;
    height: 1200px;
  }
  .cover__title {
    position: absolute;
    left: 0;
    right: 0;
    top: 1080px;
    margin: 0;
    text-align: center;
    font-family: "Cormorant Garamond", "Times New Roman", serif;
    font-weight: 500;
    font-size: 32px;
    line-height: 1;
    letter-spacing: 0.58em;
    padding-left: 0.58em;
    color: var(--title-ink);
    text-transform: uppercase;
  }
</style>
</head>
<body>
  <main class="cover">
    <svg class="cover__painting" viewBox="0 0 1200 1200" role="img"
         aria-label="Painted scene: the body of an acoustic guitar in close-up on the left, and a lone rider on horseback standing on a rock outcrop against dusky purple and rose clouds">
      <defs>
        <filter id="brushedEdge" x="-5%" y="-5%" width="110%" height="110%">
          <feTurbulence type="fractalNoise" baseFrequency="0.045 0.012" numOctaves="3" seed="7" result="streaks"/>
          <feDisplacementMap in="SourceGraphic" in2="streaks" scale="70" xChannelSelector="R" yChannelSelector="G"/>
        </filter>
        <filter id="softWash" x="-20%" y="-20%" width="140%" height="140%">
          <feGaussianBlur stdDeviation="38"/>
        </filter>
        <filter id="canvasGrain">
          <feTurbulence type="fractalNoise" baseFrequency="0.9" numOctaves="2" seed="3"/>
          <feColorMatrix values="0 0 0 0 0.15  0 0 0 0 0.1  0 0 0 0 0.3  0 0 0 0.35 0"/>
        </filter>
        <linearGradient id="duskSky" x1="0" y1="0" x2="1" y2="1">
          <stop offset="0" stop-color="var(--dusk-mid)"/>
          <stop offset="0.4" stop-color="var(--dusk-rose)"/>
          <stop offset="0.7" stop-color="var(--dusk-mid)"/>
          <stop offset="1" stop-color="var(--dusk-deep)"/>
        </linearGradient>
        <clipPath id="paintArea">
          <rect class="paint-mask" x="40" y="45" width="1120" height="1110" filter="url(#brushedEdge)"/>
        </clipPath>
        <mask id="paintMask">
          <rect x="40" y="45" width="1120" height="1110" fill="#fff" filter="url(#brushedEdge)"/>
        </mask>
      </defs>

      <g class="painting" mask="url(#paintMask)">
        <rect x="0" y="0" width="1200" height="1200" fill="url(#duskSky)"/>
        <g class="painting__washes" filter="url(#softWash)">
          <ellipse cx="620" cy="360" rx="260" ry="220" fill="var(--dusk-glow)" opacity="0.9"/>
          <ellipse cx="520" cy="470" rx="180" ry="120" fill="var(--dusk-rose)" opacity="0.8"/>
          <ellipse cx="230" cy="700" rx="260" ry="470" fill="var(--dusk-deep)" opacity="0.95"/>
          <ellipse cx="430" cy="170" rx="180" ry="140" fill="var(--dusk-ink)" opacity="0.8"/>
          <ellipse cx="1060" cy="420" rx="170" ry="140" fill="var(--dusk-ink)" opacity="0.85"/>
          <ellipse cx="860" cy="180" rx="220" ry="120" fill="var(--dusk-rose)" opacity="0.55"/>
          <ellipse cx="930" cy="760" rx="260" ry="250" fill="var(--rock-shadow)" opacity="0.9"/>
          <ellipse cx="900" cy="1020" rx="320" ry="110" fill="var(--dusk-mauve)" opacity="0.7"/>
          <ellipse cx="120" cy="90" rx="160" ry="120" fill="var(--paper)" opacity="0.5"/>
          <ellipse cx="520" cy="1110" rx="420" ry="80" fill="var(--dusk-ink)" opacity="0.8"/>
        </g>
        <rect x="0" y="0" width="1200" height="1200" filter="url(#canvasGrain)" opacity="0.6"/>
      </g>
    </svg>
    <h1 class="cover__title">Captain Wren's Parade</h1>
  </main>
</body>
</html>
```